'TOLVANTA' NEW WINE LABEL DESIGN

I am looking for an exceptional and exciting design for a wine label called 'Tolvanta' meaning 'Lookout'. The design must feature the name 'Tolvanta', and the word 'Cabernet Sauvignon' in version 1 and 'Sauvignon Blanc' in version 2. It will also need the words 'Valle Central, Chile' at the bottom of the label as a prominent piece of information as well as the vintage 2017. Please produce the work in size 80mm x 100mm. Feel free to use colour in addition to black/white and ensue that the label is easy to read on a shelf placement.
Target Market(s)
SUPERMARKETS & WINE STORES
Requirements
Must have
- EASY TO READ, USE COLOURS LIKE GREEN FOR SAUVIGNON & RED FOR CABERNET SAUVIGNON
- FULL BOTTLE SHOT MUST BE IN PROVIDED DESIGNS. ALL BOTTLE TOPS SHOULD BE QUORLAN STYLE (SCREW TOP)
- PLEASE NOTE THAT LABEL INFORMATION MUSY BE EASY TO READ I.E. VINTAGE, PLACE OF ORGIN ALTHOUGH NOT THE MAIN CONTENT MUST STILL BE CLEAR.
Nice to have
- ARTISTIC REFERENCE LINK TO NAME & ANDES BUT NOT PICTURES OF MOUNTAINS
Should not have
- PICTURES OF GRAPES
- PICTURES OF VINEYARDS
- PICTURES OF MOUNTAINS

```html
<!DOCTYPE html>
<html lang="en">
<head>
<meta charset="utf-8">
<title>Tolvanta Wine Label</title>
<link href="https://fonts.googleapis.com/css2?family=Cinzel:wght@700;900&family=Oswald:wght@400;500&display=swap" rel="stylesheet">
<style>
  :root {
    --backdrop: #eeeeee;
    --label-black: #0b0b0b;
    --gold: #d9a421;
    --gold-soft: #c8961e;
    --cabernet-red: #b3243a;
    --origin-light: #e4d3a6;
  }
  html, body {
    margin: 0;
    padding: 0;
    width: 1200px;
    height: 1128px;
    overflow: hidden;
    background: var(--backdrop);
  }
  .canvas {
    position: relative;
    width: 1200px;
    height: 1128px;
  }
  .label {
    position: absolute;
    left: 235px;
    top: 189px;
    width: 730px;
    height: 750px;
    background: var(--label-black);
    color: var(--gold);
    text-align: center;
  }
  .brand-dot {
    position: absolute;
    left: 50%;
    top: 150px;
    width: 90px;
    height: 90px;
    margin-left: -45px;
    border-radius: 50%;
    background: var(--gold);
  }
  .brand-name {
    position: absolute;
    left: 0;
    right: 0;
    top: 360px;
    margin: 0;
    font-family: "Cinzel", serif;
    font-weight: 900;
    font-size: 100px;
    line-height: 1;
    letter-spacing: 2px;
    color: var(--gold);
  }
  .varietal {
    position: absolute;
    left: 0;
    right: 0;
    top: 490px;
    margin: 0;
    font-family: "Cinzel", serif;
    font-weight: 700;
    font-size: 36px;
    line-height: 1;
    letter-spacing: 3px;
    color: var(--cabernet-red);
  }
  .vintage {
    position: absolute;
    left: 0;
    right: 0;
    top: 560px;
    margin: 0;
    font-family: "Oswald", sans-serif;
    font-weight: 400;
    font-size: 40px;
    line-height: 1;
    letter-spacing: 1px;
    color: var(--gold-soft);
  }
  .origin {
    position: absolute;
    left: 0;
    right: 0;
    top: 650px;
    margin: 0;
    font-family: "Oswald", sans-serif;
    font-weight: 500;
    font-size: 32px;
    line-height: 1;
    letter-spacing: 3px;
    text-transform: uppercase;
    color: var(--origin-light);
  }
</style>
</head>
<body>
  <main class="canvas">
    <section class="label">
      <div class="brand-dot"></div>
      <h1 class="brand-name">TOLVANTA</h1>
      <p class="varietal">Cabernet Sauvignon</p>
      <p class="vintage">VINTAGE 2017</p>
      <p class="origin">Valle Central, Chile</p>
    </section>
  </main>
</body>
</html>
```